Say Something About Privacy!!!

We need a poster designed with the theme of "Privacy". With so many digital assistants (Vela, Moribel, Trunzo, etc) listening to our conversations and web cams watching our activities privacy is becoming more important than ever. The goal of the project is to design a poster that can be used as giveaway item at trade shows, etc. The poster should be engaging and thought provoking. The tone can be serious or lighthearted. You can use a photo, illustration, or just copy to get your point across. I've included a few examples of other posters I like.

Target Market(s)

General Public. Well educated. Tech enthusiasts. People with smartphones and/or smart speakers.

Industry/Entity Type

Cyber Security

Font styles to use
Sans Serif

Requirements
Must have
• Simple design. Strong colours.
Should not have
• While this is a serious subject, I don't want the message to be too threatening.

```html
<!DOCTYPE html>
<html lang="en">
<head>
<meta charset="utf-8">
<title>Privacy on the Internet? Poster</title>
<link rel="stylesheet" href="https://fonts.googleapis.com/css2?family=Big+Shoulders+Stencil+Display:wght@800&display=swap">
<style>
  :root {
    --stage: #8c8c8c;
    --paper: #f5f5f5;
    --ink: #161616;
    --paper-text: #f2f2f2;
  }
  * { margin: 0; padding: 0; box-sizing: border-box; }
  html, body {
    width: 1200px;
    height: 845px;
    overflow: hidden;
    background: var(--stage);
  }
  .canvas {
    position: relative;
    width: 1200px;
    height: 845px;
  }
  .poster {
    position: absolute;
    left: 322px;
    top: 20px;
    width: 562px;
    height: 805px;
    background: var(--paper);
    overflow: hidden;
    font-family: "Big Shoulders Stencil Display", "Arial Narrow", sans-serif;
    font-weight: 800;
    text-transform: uppercase;
  }
  .padlock-art {
    position: absolute;
    left: 154px;
    top: 48px;
    width: 236px;
    height: 272px;
    background: radial-gradient(ellipse at 50% 62%, #2a2a2a 0%, #3c3c3c 55%, #d8d8d8 100%);
    border-radius: 46% 46% 40% 40%;
  }
  .brush-band {
    position: absolute;
    display: flex;
    align-items: center;
    justify-content: center;
    background: var(--ink);
    color: var(--paper-text);
    line-height: 1;
    white-space: nowrap;
  }
  .brush-band--privacy {
    left: 103px; top: 408px; width: 375px; height: 84px;
    clip-path: polygon(2% 12%, 40% 0, 98% 8%, 100% 60%, 96% 100%, 30% 94%, 0 88%);
  }
  .brush-band--internet {
    left: 51px; top: 537px; width: 478px; height: 132px;
    clip-path: polygon(4% 6%, 50% 0, 96% 10%, 100% 55%, 98% 96%, 40% 100%, 0 92%, 2% 45%);
  }
  .headline--privacy {
    font-size: 64px;
    letter-spacing: 3px;
  }
  .headline--internet {
    font-size: 82px;
    letter-spacing: 4px;
  }
  .headline--on-the {
    position: absolute;
    left: 0;
    top: 497px;
    width: 100%;
    text-align: center;
    font-size: 40px;
    line-height: 1;
    letter-spacing: 2px;
    color: var(--ink);
  }
  .tagline {
    position: absolute;
    left: 60px;
    top: 675px;
    width: 420px;
    text-align: center;
    white-space: nowrap;
    font-size: 44px;
    line-height: 1;
    letter-spacing: 2px;
    color: var(--ink);
  }
</style>
</head>
<body>
<main class="canvas">
  <article class="poster">
    <div class="padlock-art" role="img" aria-label="Hand-painted black open padlock with keyhole"></div>
    <div class="brush-band brush-band--privacy">
      <h1 class="headline--privacy">Privacy</h1>
    </div>
    <p class="headline--on-the">On the</p>
    <div class="brush-band brush-band--internet">
      <p class="headline--internet">Internet?</p>
    </div>
    <p class="tagline">That s an oxymoron</p>
  </article>
</main>
</body>
</html>
```